Educational Institution needs a new website

A little bit about ourselves:
Bramwell College is a multicultural K-12 school with students who represent nearly 30 ethnic and cultural backgrounds. It is one of the fastest growing schools in the City of Torvale (in Perth, Western Australia), and offers quality education with a unique school environment at two campuses.
The mission of Bramwell College is to equip students with moral values, academic knowledge and 21st century skills. We empower students to unlock their potential to be confident global citizens.
Bramwell College strives to educate students in a manner which inspires them to become lifelong learners. We are committed to raising individuals who are tolerant and respectful towards others enabling them to grow into citizens who contribute to the common good of society.
Here are our design goals:
#1: To emphasise the growth of the school from a small school community to a much larger prestigious college.
#2: Have current and prospective parents have a clear understanding of our college’s morals and values and how we differ from other colleges.
#3: Highlight that our school provides a joyful and safe environment, which is highly valued by parents.
#4: Emphasise that our school presents a welcoming atmosphere for parents as we have strong relationships with our community.
#5: Highlight the various after-school activities available to our students, which are provided through the clubs and pastoral care department.
#6: Allow for online registrations and the option of adding student, staff and parent portals.
#7: Follow the existing school colours
We would like to request the design for the home page and a secondary page to see the alternative layouts.
Other information:
Please note that our logo is will be changed slightly in the upcoming weeks. Please keep this in mind while designing.
We will have another contest for the coding of the website.
We want to be able to make amendments and additions to the content of the website in the future and would like to make sure we have a strong communication with the designer.
The existing website is https://www.bramwellcol.example.edu.au/ for reference for school colours and content.
Industry/Entity Type
Education
Number of Pages Required
1 page

```html
<!DOCTYPE html>
<html lang="en">
<head>
<meta charset="utf-8">
<title>Bramwell College</title>
<link href="https://fonts.googleapis.com/css2?family=Poppins:ital,wght@0,400;0,500;0,600;0,700;1,400&display=swap" rel="stylesheet">
<style>
:root{
  --navy:#0b1d36;
  --topbar:#0d50a8;
  --panel:#0a72b9;
  --accent:#0aa3dc;
  --accent-soft:#5cc3e8;
  --text:#2a2f38;
  --line:#9fd3ee;
  --white:#ffffff;
}
*{margin:0;padding:0;box-sizing:border-box}
html,body{width:1200px;height:4254px;overflow:hidden}
body{position:relative;font-family:"Poppins",sans-serif;color:var(--text);background:var(--white)}
.abs{position:absolute}
a{color:inherit}
.topbar{left:0;top:0;width:1200px;height:41px;background:var(--topbar);color:var(--white);font-size:11px}
.topbar .contact{position:absolute;top:13px;display:flex;align-items:center;gap:7px}
.topbar .social{position:absolute;right:188px;top:10px;display:flex;gap:5px}
.topbar .social span{width:20px;height:20px;border:1.5px solid var(--white);border-radius:50%}
.brand{display:flex;align-items:center;gap:10px;font-weight:700;color:var(--accent)}
.brand .dot{width:34px;height:34px;border-radius:50%;background:var(--accent)}
.brand .name{font-size:23px;line-height:1;letter-spacing:.5px}
.nav{top:66px;left:186px;width:826px;height:58px;display:flex;align-items:center}
.nav ul{display:flex;list-style:none;gap:26px;margin-left:66px;font-size:12px;color:var(--navy)}
.nav ul li:first-child{font-weight:600}
.nav .tools{margin-left:auto;display:flex;align-items:center;gap:14px}
.btn{display:inline-flex;align-items:center;gap:8px;background:var(--accent);color:var(--white);font-size:12px;font-weight:500;border-radius:6px;text-decoration:none;justify-content:center}
.btn svg{width:14px;height:14px}
.hero{left:63px;top:150px;width:1074px;height:576px;border:2px solid var(--line);border-radius:34px;overflow:hidden;background:linear-gradient(135deg,#eef6fb 0%,#dbe9f2 45%,#c9d9e5 70%,#b9c9d6 100%)}
.hero h1{position:absolute;left:123px;top:66px;font-size:50px;font-weight:700;line-height:1.2;color:var(--navy);letter-spacing:-1px}
.hero h1 em{font-style:normal;color:var(--accent)}
.hero .links{position:absolute;left:123px;top:190px;display:flex;gap:26px;font-size:11.5px;color:var(--navy)}
.hero .links a{text-decoration:underline}
h2{font-size:40px;font-weight:700;line-height:1.2;color:var(--navy);letter-spacing:-.8px}
h2 em{font-style:normal;color:var(--accent)}
p{font-size:11.5px;line-height:1.45}
.welcome{left:260px;top:817px;width:680px;text-align:center}
.welcome p{margin:18px auto 22px;width:640px}
.welcome .btn{width:116px;height:36px}
.about{left:186px;top:1186px;width:340px}
.about p{margin:16px 0 22px}
.about .btn{width:117px;height:37px}
.photo{border-radius:26px}
.pathway{left:186px;top:1615px;width:825px;height:349px;background:var(--panel);border-radius:22px;color:var(--white);text-align:center}
.pathway h2{color:var(--white);margin-top:52px}
.pathway p{width:620px;margin:16px auto 0}
.pathway .values{font-style:italic;font-size:15.5px;line-height:1.45;width:600px;margin:20px auto 0}
.environment{left:607px;top:2060px;width:420px}
.environment p{margin:16px 0 0;width:400px}
.features{display:grid;grid-template-columns:208px 208px;row-gap:8px;margin-top:18px}
.feature{display:flex;align-items:center;gap:16px;font-size:14px;color:var(--navy)}
.feature .ic{width:53px;height:53px;border-radius:12px;background:var(--topbar);display:flex;align-items:center;justify-content:center}
.feature .ic.light{background:var(--accent-soft)}
.feature .ic svg{width:24px;height:24px}
.activities-head{left:186px;top:2492px;width:600px}
.activities-head p{margin-top:6px;width:580px}
.card{width:264px;height:284px;border:2px solid var(--line);border-radius:22px;overflow:hidden}
.card .pic{margin:5px;height:224px;border-radius:18px}
.card .meta{display:flex;align-items:center;padding:12px 22px 0 24px;font-size:14px;color:var(--navy)}
.card .meta a{margin-left:auto;font-size:11px;text-decoration:underline}
.registration{left:186px;top:3331px;width:825px;height:697px;background:var(--panel);border-radius:24px;color:var(--white)}
.registration h2{color:var(--white);text-align:center;margin-top:58px;font-size:42px}
.registration .sub{text-align:center;font-size:11.5px;margin-top:2px}
.label{position:absolute;left:71px;font-size:14px}
.field{position:absolute;width:334px;height:40px;background:var(--white);border-radius:3px;font-size:11px;color:#7fa6c6;padding:12px 18px}
.check{position:absolute;left:71px;display:flex;align-items:center;gap:10px;font-size:11px}
.check span{width:17px;height:17px;background:var(--white);border-radius:3px}
.terms{position:absolute;left:561px;top:528px;width:194px;height:52px;background:var(--accent);border-radius:6px;display:flex;align-items:center;justify-content:center;font-size:14px}
.submit{position:absolute;left:561px;top:601px;width:194px;height:36px;background:var(--white);color:var(--panel);border-radius:6px;display:flex;align-items:center;justify-content:center;gap:8px;font-size:12px;font-weight:500}
.footer{left:0;top:4112px;width:1200px;text-align:center}
.footer .brand{justify-content:center}
.footer small{display:block;margin-top:30px;font-size:11.5px;color:var(--navy)}
</style>
</head>
<body>

<header class="abs topbar">
  <div class="contact" style="left:188px">
    <svg width="12" height="12" viewBox="0 0 24 24" fill="#fff"><path d="M6.6 10.8a15 15 0 0 0 6.6 6.6l2.2-2.2a1 1 0 0 1 1-.25 11.4 11.4 0 0 0 3.6.57 1 1 0 0 1 1 1V20a1 1 0 0 1-1 1A17 17 0 0 1 3 4a1 1 0 0 1 1-1h3.5a1 1 0 0 1 1 1c0 1.25.2 2.45.57 3.57a1 1 0 0 1-.25 1z"/></svg>
    (08) 9000 4172
  </div>
  <div class="contact" style="left:314px">
    <svg width="12" height="10" viewBox="0 0 24 20" fill="#fff"><path d="M2 0h20a2 2 0 0 1 2 2v16a2 2 0 0 1-2 2H2a2 2 0 0 1-2-2V2a2 2 0 0 1 2-2zm10 9L22 3H2z"/></svg>
    admin@bramwell.example.edu.au
  </div>
  <div class="social"><span></span><span></span><span></span></div>
</header>

<nav class="abs nav">
  <div class="brand"><span class="dot"></span><span class="name">BRAMWELL<br><span style="font-size:15px;letter-spacing:5px">COLLEGE</span></span></div>
  <ul><li>Home</li><li>Welcome</li><li>About</li><li>Values</li><li>Learning</li><li>Activities</li></ul>
  <div class="tools">
    <svg width="18" height="14" viewBox="0 0 18 14" stroke="#0b1d36" stroke-width="2"><path d="M0 1h18M0 7h18M0 13h18"/></svg>
    <svg width="16" height="16" viewBox="0 0 16 16" fill="none" stroke="#0b1d36" stroke-width="1.6"><circle cx="8" cy="5" r="3.5"/><path d="M1.5 15.5a6.5 6.5 0 0 1 13 0"/></svg>
    <svg width="16" height="16" viewBox="0 0 16 16" fill="none" stroke="#0b1d36" stroke-width="2"><circle cx="7" cy="7" r="5"/><path d="M11 11l4 4"/></svg>
    <a class="btn" style="width:116px;height:37px;margin-left:8px">Join Us Now <svg viewBox="0 0 14 14" fill="none" stroke="#fff" stroke-width="1.4"><rect x="1" y="1" width="12" height="12" rx="3"/><path d="M4 7h6M7.5 4.5 10 7l-2.5 2.5"/></svg></a>
  </div>
</nav>

<section class="abs hero" role="img" aria-label="Teacher and young students gathered around a classroom table with books and a globe">
  <h1>A Journey Of Learning,<br><em>Growing</em>, And Achieving!</h1>
  <div class="links"><a>Kindagarden</a><a>Primary Curriculum</a><a>Secondary Curriculum</a><a>Wace</a></div>
</section>

<section class="abs welcome">
  <h2>Welcome to Our <em>Bramwell</em><br><em>College</em></h2>
  <p>It is with great pleasure that I welcome you to the Bramwell College website. We at Bramwell College are constantly in search of better ways to educate and prepare our students for life in the 21st century, where we believe that only individuals with soft skills (such as creativity, collaboration, communication and critical thinking) will be able to reach their full potential. Although this is a challenging aim, education is not a formidable matter as long as you are devoted enough. In my opinion, it is all about love and care. If a student is educated by teachers equipped with these powerful tools, there is no reason why they cannot be successful.</p>
  <a class="btn">Read More <svg viewBox="0 0 14 14" fill="none" stroke="#fff" stroke-width="1.4"><rect x="1" y="1" width="12" height="12" rx="3"/><path d="M4 7h6M7.5 4.5 10 7l-2.5 2.5"/></svg></a>
</section>

<section class="abs about">
  <h2>About <em>Bramwell</em><br><em>College</em></h2>
  <p>Meridian Education and Culture Foundation was founded in 2001 by a group of Turkish-Australians who wished to contribute to the community, particularly in the field of education. In 2006, the Foundation established Brook College, naming the new school after the word for 'droplet'. The founding principle of the College was to raise morally and socially responsible students academically equipped to be contributing citizens. When it opened, Brook College had an enrolment of 33 students.</p>
  <a class="btn">Read More <svg viewBox="0 0 14 14" fill="none" stroke="#fff" stroke-width="1.4"><rect x="1" y="1" width="12" height="12" rx="3"/><path d="M4 7h6M7.5 4.5 10 7l-2.5 2.5"/></svg></a>
</section>
<div class="abs photo" style="left:558px;top:1183px;width:453px;height:330px;background:linear-gradient(160deg,#b7a58c 0%,#8e9c7a 40%,#b9b2a6 75%,#d8d2c8 100%)" role="img" aria-label="Group of school children with backpacks running along a path outside school"></div>

<section class="abs pathway">
  <h2>The Pathway to Trust<br>and Integrity</h2>
  <p>Moral values are principles or beliefs that guide individuals in determining what is right or wrong and how to behave in various situations. These values provide a framework for ethical decision-making and shape our character, actions, and interactions with others. Some of the Moral Values of our college are:</p>
  <p class="values">Integrity, Care, Excellence, Creativity, Critical Thinking, Resilience, Self-Discipline, Self-Esteem, Serving Fellow Humans, Tolerance, Peace, Respect, Social Harmony, Health and Wellbeing.</p>
</section>

<div class="abs photo" style="left:186px;top:2064px;width:396px;height:338px;background:linear-gradient(150deg,#5f8a3a 0%,#9cbf48 35%,#e5e04a 55%,#d86a8c 80%,#3f6f2a 100%)" role="img" aria-label="Cheerful children raising their arms outdoors among greenery"></div>
<section class="abs environment">
  <h2>Providing Unique<br>Learning <em>Environment</em></h2>
  <p>A joyful environment in schools is crucial for the overall well-being and development of children. It involves creating a positive atmosphere, engaging teaching methods, celebrating diversity, encouraging play and physical activity, cultivating positive relationships, incorporating creative expression and artistic activities, celebrating achievements, and ensuring a safe and supportive environment. It also include:</p>
  <div class="features">
    <div class="feature"><span class="ic"><svg viewBox="0 0 24 24" fill="#fff"><path d="M6 2h12v3h4v3a5 5 0 0 1-5 5 6 6 0 0 1-4 3v3h4v3H7v-3h4v-3a6 6 0 0 1-4-3 5 5 0 0 1-5-5V5h4zM4 7v1a3 3 0 0 0 2 2.8V7zm16 0h-2v3.8A3 3 0 0 0 20 8z"/></svg></span>Active Learning</div>
    <div class="feature"><span class="ic"><svg viewBox="0 0 24 24" fill="#fff"><circle cx="12" cy="7" r="5"/><path d="M3 23a9 9 0 0 1 18 0z"/></svg></span>Expert Teachers</div>
    <div class="feature"><span class="ic light"><svg viewBox="0 0 24 24" fill="#fff"><circle cx="8" cy="6" r="3.5"/><circle cx="17" cy="9" r="2.8"/><path d="M2 22v-5a6 6 0 0 1 12 0v5zM14 22v-4a4 4 0 0 1 8 0v4z"/></svg></span>Parents Day</div>
    <div class="feature"><span class="ic light"><svg viewBox="0 0 24 24" fill="#fff"><path d="M9 3l12-2v15a3 3 0 1 1-2-2.8V6l-8 1.4V18a3 3 0 1 1-2-2.8z"/></svg></span>Music Lessons</div>
  </div>
</section>

<section class="abs activities-head">
  <h2>Our <em>Activities</em></h2>
  <p>Here at Bramwell College, clubs focus on students having fun and building friendships, learning skills or getting some exercise. Clubs and Pastoral care are run by teachers and or volunteers and are always overseen by teachers. In this way students can pursue a variety of areas of personal interest in a supervised environment such as:</p>
</section>
<a class="abs btn" style="left:840px;top:2559px;width:166px;height:41px">View All Activities <svg viewBox="0 0 14 14" fill="none" stroke="#fff" stroke-width="1.4"><rect x="1" y="1" width="12" height="12" rx="3"/><path d="M4 7h6M7.5 4.5 10 7l-2.5 2.5"/></svg></a>

<div class="abs card" style="left:186px;top:2643px"><div class="pic" style="background:linear-gradient(180deg,#9cc6e8,#d8b47a 60%,#4d7fb3)" role="img" aria-label="Two boys in hats fishing by a lake"></div><div class="meta">Fishing<a>See More ↗</a></div></div>
<div class="abs card" style="left:467px;top:2643px"><div class="pic" style="background:linear-gradient(180deg,#e8e8e6,#b9bcbf 60%,#6f8a74)" role="img" aria-label="Children dancing in a bright studio"></div><div class="meta">Dancing<a>See More ↗</a></div></div>
<div class="abs card" style="left:747px;top:2643px"><div class="pic" style="background:linear-gradient(180deg,#eef0ef,#c9cfd6 55%,#5b8fc9)" role="img" aria-label="Children drawing with coloured pencils at a table"></div><div class="meta">Art &amp; Craft<a>See More ↗</a></div></div>
<div class="abs card" style="left:186px;top:2949px"><div class="pic" style="background:linear-gradient(135deg,#3e5a4a,#7e9a8c 50%,#d7a3b6)" role="img" aria-label="Student speaking through a megaphone to classmates by a chalkboard"></div><div class="meta">Debating<a>See More ↗</a></div></div>
<div class="abs card" style="left:467px;top:2949px"><div class="pic" style="background:linear-gradient(180deg,#c4d4e0,#b78c80 50%,#8a5a4e)" role="img" aria-label="Students reading together at a classroom desk"></div><div class="meta">Pastoral Care<a>See More ↗</a></div></div>
<div class="abs card" style="left:747px;top:2949px"><div class="pic" style="background:linear-gradient(180deg,#8f9aa6,#6f7b88 50%,#5a6c85)" role="img" aria-label="Two girls taking photos with a camera against a wooden wall"></div><div class="meta">Photography<a>See More ↗</a></div></div>

<section class="abs registration">
  <h2>Registration Form</h2>
  <p class="sub">Please fill out the following information to register:</p>
  <div class="label" style="top:144px">Student Information:</div>
  <div class="field" style="left:71px;top:172px">Student Name</div>
  <div class="field" style="left:421px;top:172px">Student ID</div>
  <div class="field" style="left:71px;top:235px">Course/Program</div>
  <div class="field" style="left:421px;top:235px">Grade Level</div>
  <div class="field" style="left:71px;top:297px">Phone Number</div>
  <div class="field" style="left:421px;top:297px">Email</div>
  <div class="label" style="top:365px">Parents Information:</div>
  <div class="field" style="left:71px;top:393px">Name</div>
  <div class="field" style="left:421px;top:393px">Email</div>
  <div class="field" style="left:71px;top:456px">Phone Number</div>
  <div class="field" style="left:421px;top:456px">CNIC</div>
  <div class="label" style="top:525px">I agree with the following statements:</div>
  <div class="check" style="top:560px"><span></span>I am the parent/guardian of the child indicated above.</div>
  <div class="check" style="top:588px"><span></span>I agree with that; the provided information is correct.</div>
  <div class="check" style="top:616px"><span></span>I agree with your all Terms &amp; Conditions.</div>
  <div class="terms">Term &amp; Conditions</div>
  <div class="submit">Submit Form <svg width="14" height="14" viewBox="0 0 14 14" fill="none" stroke="#0a72b9" stroke-width="1.4"><rect x="1" y="1" width="12" height="12" rx="3"/><path d="M4 7h6M7.5 4.5 10 7l-2.5 2.5"/></svg></div>
</section>

<footer class="abs footer">
  <div class="brand"><span class="dot"></span><span class="name" style="text-align:left">BRAMWELL<br><span style="font-size:15px;letter-spacing:5px">COLLEGE</span></span></div>
  <small>All rights reserved Copyright © 2023</small>
</footer>

</body>
</html>
```